Women's Online Clothing Boutique Needs Business Cards

I already have a logo that I would like to use. Some of the things that interest me is black business cards, foil embossed logo, glossy embossed logo, leopard print, no yellow font, rounded edges. I even like just a large logo on the front side with all of my information on the back side.

Contact Information for Business Card

https://silverheron.shopvenlo.com/
https://www.pagelink.net/thesilverheronboutique/
https://www.picfeed.net/thesilverheronboutique/
silverheronboutique@mailora.net

Requirements
Must have
• My Logo
Nice to have
• Leopard Print
Should not have
• No Yellow Font

```html
<!DOCTYPE html>
<html lang="en">
<head>
<meta charset="utf-8">
<title>The Silver Heron Boutique – Business Card Proof</title>
<link rel="stylesheet" href="https://fonts.googleapis.com/css2?family=Josefin+Sans:wght@400&family=Cormorant+Garamond:wght@500&family=Roboto+Condensed:wght@400&family=Roboto:wght@300&display=swap">
<style>
  :root {
    --page: #ffffff;
    --card: #efe4bd;
    --ink: #1c1a17;
    --gold: #c4912f;
    --gold-light: #e2b84e;
    --gold-dark: #a87a22;
    --note: #5d5d5d;
  }
  * { box-sizing: border-box; margin: 0; padding: 0; }
  html, body {
    width: 1200px;
    height: 875px;
    overflow: hidden;
    background: var(--page);
  }
  .proof-sheet {
    position: relative;
    width: 1200px;
    height: 875px;
  }
  .card {
    position: absolute;
    left: 158px;
    width: 736px;
    height: 421px;
    background: var(--card);
    border-radius: 28px;
  }
  .card--front { top: 0; }
  .card--back { top: 454px; }

  /* Front */
  .front-artwork {
    position: absolute;
    left: 289px;
    top: 105px;
    width: 214px;
    height: 112px;
    border-radius: 48px 60px 20px 40px;
    background: linear-gradient(120deg, var(--gold-dark), var(--gold-light) 45%, var(--gold) 70%, var(--gold-dark));
  }
  .wordmark {
    position: absolute;
    left: 0;
    top: 190px;
    width: 736px;
    text-align: center;
    font-family: "Josefin Sans", sans-serif;
    font-weight: 400;
    color: var(--ink);
    line-height: 1;
  }
  .wordmark__name {
    display: block;
    font-size: 58px;
    letter-spacing: -1px;
  }
  .wordmark__sub {
    display: block;
    margin-top: 14px;
    font-size: 34px;
  }

  /* Back */
  .back-artwork {
    position: absolute;
    left: 42px;
    top: 205px;
    width: 238px;
    height: 126px;
    border-radius: 40px 70px 24px 50px;
    background: var(--gold);
  }
  .back-title {
    position: absolute;
    left: 371px;
    top: 76px;
    font-family: "Cormorant Garamond", serif;
    font-weight: 500;
    font-size: 44px;
    letter-spacing: 1px;
    color: var(--ink);
    white-space: nowrap;
  }
  .contact-list {
    position: absolute;
    left: 371px;
    top: 182px;
    list-style: none;
  }
  .contact-item {
    display: flex;
    align-items: center;
    height: 26px;
    margin-bottom: 23px;
    font-family: "Roboto Condensed", sans-serif;
    font-size: 18.5px;
    color: var(--ink);
    white-space: nowrap;
  }
  .contact-item:last-child { margin-bottom: 0; }
  .contact-icon {
    width: 26px;
    height: 26px;
    margin-right: 15px;
    flex: none;
  }

  /* Production notes */
  .note {
    position: absolute;
    font-family: "Roboto", sans-serif;
    font-weight: 300;
    font-size: 20px;
    line-height: 27px;
    color: var(--note);
    white-space: nowrap;
  }
  .note--front { left: 915px; top: 169px; }
  .note--back { left: 915px; top: 649px; }
  .note--artwork { left: 0; top: 700px; }
</style>
</head>
<body>
<main class="proof-sheet">

  <section class="card card--front" aria-label="Card front">
    <div class="front-artwork" role="img" aria-label="Gold leaf illustration of a reclining leopard resting on a branch"></div>
    <h1 class="wordmark">
      <span class="wordmark__name">The Silver Heron</span>
      <span class="wordmark__sub">Boutique</span>
    </h1>
  </section>

  <section class="card card--back" aria-label="Card back">
    <div class="back-artwork" role="img" aria-label="Gold silhouette of a reclining leopard on a branch"></div>
    <h2 class="back-title">SILVER HERON</h2>
    <ul class="contact-list">
      <li class="contact-item">
        <svg class="contact-icon" viewBox="0 0 26 26" aria-hidden="true">
          <g fill="none" stroke="#1c1a17" stroke-width="1.6">
            <circle cx="13" cy="13" r="11.5"/>
            <ellipse cx="13" cy="13" rx="5" ry="11.5"/>
            <line x1="1.5" y1="13" x2="24.5" y2="13"/>
            <line x1="3.5" y1="7" x2="22.5" y2="7"/>
            <line x1="3.5" y1="19" x2="22.5" y2="19"/>
          </g>
        </svg>
        https://silverheron.shopvenlo.com/
      </li>
      <li class="contact-item">
        <svg class="contact-icon" viewBox="0 0 26 26" aria-hidden="true">
          <rect x="1" y="1" width="24" height="24" rx="4" fill="#1c1a17"/>
        </svg>
        thesilverheronboutique/
      </li>
      <li class="contact-item">
        <svg class="contact-icon" viewBox="0 0 26 26" aria-hidden="true">
          <circle cx="13" cy="13" r="11.5" fill="none" stroke="#1c1a17" stroke-width="2.4"/>
        </svg>
        thesilverheronboutique/
      </li>
      <li class="contact-item">
        <svg class="contact-icon" viewBox="0 0 26 26" aria-hidden="true">
          <rect x="1.5" y="4" width="23" height="18" rx="1.5" fill="none" stroke="#1c1a17" stroke-width="2.4"/>
          <polyline points="2.5,5.5 13,14 23.5,5.5" fill="none" stroke="#1c1a17" stroke-width="2.4"/>
        </svg>
        silverheronboutique@mailora.net
      </li>
    </ul>
  </section>

  <p class="note note--front">Leopard image<br>go for Gold leaf &amp;<br>All text go for Emboss</p>
  <p class="note note--back">All text with Icon go for Emboss</p>
  <p class="note note--artwork">Leopard<br>image go for<br>Gold&nbsp; emboss</p>

</main>
</body>
</html>
```